Commercial Construction Company

We need a business card design based on our current logo. We are a commercial general contractor based in Southern California that specializes in bank remodels. We would like to see designs that incorporate dark blue. The final design should portray an image of professionalism and quality.

If possible, I would like to add metallic foil to the design. Thank you

```html
<!DOCTYPE html>
<html lang="en">
<head>
<meta charset="utf-8">
<title>Harbor Ridge Construction Services – Business Card</title>
<link href="https://fonts.googleapis.com/css2?family=Montserrat:wght@400;500;800&display=swap" rel="stylesheet">
<style>
  :root {
    --navy: #0b0b96;
    --bright-blue: #3a8cf0;
    --sky-top: #7fb0de;
    --sky-mid: #d9e6f2;
    --tower: #5f7d99;
    --white: #ffffff;
    --ink: #14215e;
    --page: #ffffff;
  }
  * { margin: 0; padding: 0; box-sizing: border-box; }
  html, body { width: 891px; height: 1200px; overflow: hidden; background: var(--page); }
  body { position: relative; font-family: "Montserrat", sans-serif; }
  .card {
    position: absolute;
    left: 30px;
    width: 831px;
    height: 475px;
    overflow: hidden;
  }
  .card--front { top: 110px; }
  .card--back { top: 630px; }
  .card__art { position: absolute; inset: 0; width: 100%; height: 100%; }
  .brand {
    position: absolute;
    left: 48px;
    top: 318px;
    width: 200px;
    text-align: center;
  }
  .brand__name {
    font-weight: 800;
    font-size: 58px;
    letter-spacing: 1px;
    color: var(--ink);
    line-height: 1;
  }
  .contacts {
    position: absolute;
    left: 16px;
    top: 214px;
    list-style: none;
    color: var(--white);
    font-size: 17px;
    font-weight: 500;
  }
  .contacts__item {
    display: flex;
    align-items: flex-start;
    gap: 12px;
    margin-bottom: 19px;
  }
  .contacts__icon { width: 26px; height: 26px; flex: none; }
  .contacts__text { line-height: 1.25; padding-top: 3px; }
  .contacts__item--note .contacts__text { width: 290px; }
</style>
</head>
<body>

  <section class="card card--front" aria-label="Card front">
    <svg class="card__art" viewBox="0 0 831 475" preserveAspectRatio="none">
      <defs>
        <linearGradient id="skyFront" x1="0" y1="0" x2="0.3" y2="1">
          <stop offset="0" stop-color="var(--sky-top)"/>
          <stop offset="0.5" stop-color="var(--sky-mid)"/>
          <stop offset="1" stop-color="var(--tower)"/>
        </linearGradient>
      </defs>
      <rect width="831" height="475" fill="url(#skyFront)" role="img" aria-label="Photo of glass skyscrapers against a cloudy blue sky"/>
      <polygon points="0,0 134,0 445,475 0,475" fill="var(--bright-blue)"/>
      <polygon points="0,0 150,0 0,113" fill="var(--navy)"/>
      <polygon points="445,475 831,246 831,475" fill="var(--navy)"/>
    </svg>
    <div class="brand">
      <div class="brand__name">HRCS</div>
    </div>
  </section>

  <section class="card card--back" aria-label="Card back">
    <svg class="card__art" viewBox="0 0 831 475" preserveAspectRatio="none">
      <defs>
        <linearGradient id="skyBack" x1="0" y1="0" x2="0.3" y2="1">
          <stop offset="0" stop-color="var(--sky-top)"/>
          <stop offset="0.5" stop-color="var(--sky-mid)"/>
          <stop offset="1" stop-color="var(--tower)"/>
        </linearGradient>
      </defs>
      <rect width="831" height="475" fill="url(#skyBack)" role="img" aria-label="Photo of glass skyscrapers against a cloudy blue sky"/>
      <polygon points="0,0 252,0 609,475 0,475" fill="var(--navy)"/>
    </svg>

    <ul class="contacts">
      <li class="contacts__item">
        <svg class="contacts__icon" viewBox="0 0 24 24" fill="var(--white)" aria-hidden="true">
          <path d="M6.6 10.8a15.1 15.1 0 0 0 6.6 6.6l2.2-2.2c.3-.3.7-.4 1-.2 1.1.4 2.3.6 3.6.6.6 0 1 .4 1 1V20c0 .6-.4 1-1 1A17 17 0 0 1 3 4c0-.6.4-1 1-1h3.5c.6 0 1 .4 1 1 0 1.2.2 2.4.6 3.6.1.3 0 .7-.2 1l-2.3 2.2z"/>
        </svg>
        <span class="contacts__text">+ 123 4567890</span>
      </li>
      <li class="contacts__item">
        <svg class="contacts__icon" viewBox="0 0 24 24" fill="none" stroke="var(--white)" stroke-width="1.8" aria-hidden="true">
          <rect x="2.5" y="5" width="19" height="14" rx="1"/>
          <path d="M2.5 6l9.5 7 9.5-7"/>
        </svg>
        <span class="contacts__text">hello@harborridge.com</span>
      </li>
      <li class="contacts__item">
        <svg class="contacts__icon" viewBox="0 0 24 24" fill="none" stroke="var(--white)" stroke-width="1.6" aria-hidden="true">
          <circle cx="12" cy="12" r="9.5"/>
          <ellipse cx="12" cy="12" rx="4.2" ry="9.5"/>
          <path d="M2.5 12h19M4 7h16M4 17h16"/>
        </svg>
        <span class="contacts__text">www.harborridge.com</span>
      </li>
      <li class="contacts__item contacts__item--note">
        <svg class="contacts__icon" viewBox="0 0 24 24" fill="none" stroke="var(--white)" stroke-width="1.7" aria-hidden="true">
          <rect x="3" y="4" width="18" height="16" rx="1"/>
          <path d="M3 8h18M7 12h4v5H7zM14 12h3M14 15h3"/>
        </svg>
        <span class="contacts__text">Lorem Ipsum is simply dummy text of the printing and typesetting industry.</span>
      </li>
    </ul>
  </section>

</body>
</html>
```